Personal Motivational Quote Poster Design

I would like to create a poster with some of my favorite quotes to hang in my office. I did similar projects in 2012 and 2014. I've uploaded the winning designs so you can get a better idea of what I'm looking for. I will provide feedback on your design within 24 hours of receiving it.

The poster must contain the following quotes:

“What the pupil must learn, if he learns anything at all, is that the world will do most of the work for you, provided you cooperate with it by identifying how it really works and aligning with those realities. If we do not let the world teach us, it teaches us a lesson.” - Harold Wexbury

“I tackle every big new problem by asking two questions: Who has dealt with this problem well? And what can we learn from them?” - Tom Harlow

“If we can really understand the problem, the answer will come out of it, because the answer is not separate from the problem.” - Ravindra Pallathuri

“Success is nothing more than a few simple disciplines, practiced every day; while failure is simply a few errors in judgment, repeated every day. It is the accumulative weight of our disciplines and our judgments that leads us to either fortune or failure.” - Ned Pilsk

“Inaction breeds doubt and fear. Action breeds confidence and courage.” - Walt Brimsley

“What’s the one thing you can do, such that by doing it, everything else will be easier or unnecessary?” - Lenny Druse

Requirements
Must have
• The poster will be 24" high x 36" long and printed on canvas, so the image you create needs to have a resolution of at least 2700 x 3900.
Nice to have
• I don't have an exact vision for how the poster should look, so I am totally open to you using your creativity to develop, arrange and present the content as you'd like.

That said, I would like an image (photo or posterized image) of the person being quoted along with each quote. I do not have specific images that I would like you to use, so you will need to find the images on your own.

The images don't need to be perfect... I am more interested in the poster relating the essence of the quotes and the people being quoted than I am in perfect photographic images of the people being quoted.

```html
<!DOCTYPE html>
<html lang="en">
<head>
<meta charset="utf-8">
<title>Favorite Quotes Poster</title>
<link href="https://fonts.googleapis.com/css2?family=Noto+Serif:ital@1&family=Open+Sans:wght@400;600&display=swap" rel="stylesheet">
<style>
  :root {
    --page: #ffffff;
    --stripe-a: #f88fb0;
    --stripe-b: #fba3bf;
    --sky: #d5f3fb;
    --lemon: #fbee8c;
    --mist: #e9eaea;
    --lime: #d9df85;
    --lavender: #d1cce4;
    --ink: #7a7a7a;
    --ink-dark: #555555;
    --shadow: rgba(120, 40, 70, 0.35);
  }
  * { box-sizing: border-box; margin: 0; padding: 0; }
  html, body { width: 800px; height: 1200px; overflow: hidden; background: var(--page); }
  .canvas { position: relative; width: 800px; height: 1200px; }
  .poster {
    position: absolute; left: 48px; top: 45px; width: 704px; height: 1108px;
    border-radius: 14px;
    background: repeating-linear-gradient(90deg, var(--stripe-a) 0 11px, var(--stripe-b) 11px 22px);
  }
  .bubble {
    position: absolute; border-radius: 14px;
    box-shadow: 3px 4px 6px var(--shadow);
  }
  .bubble .tail { position: absolute; overflow: visible; }
  .quote {
    position: absolute;
    font-family: "Noto Serif", Georgia, serif; font-style: italic;
    color: var(--ink); font-size: 14.5px; line-height: 22px; white-space: nowrap;
  }
  .author {
    position: absolute; font-family: "Open Sans", Arial, sans-serif;
    font-size: 6.5px; line-height: 8px; letter-spacing: 0.3px; color: var(--ink-dark); text-transform: uppercase;
    white-space: nowrap;
  }
  .portrait { position: absolute; }

  .bubble--pupil { left: 127px; top: 100px; width: 541px; height: 155px; background: var(--sky); }
  .bubble--pupil .quote { left: 32px; top: 24px; }
  .bubble--pupil .author { right: 60px; top: 135px; }
  .bubble--pupil .portrait { left: 438px; top: 27px; width: 76px; height: 100px;
    background: linear-gradient(160deg, #8a8a8a, #2a2a2a); }
  .bubble--pupil .tail { left: 48px; top: 154px; }

  .bubble--problems { left: 93px; top: 280px; width: 604px; height: 130px; background: var(--lemon);
    border-radius: 2px; transform: rotate(-1.6deg); }
  .bubble--problems .quote { left: 168px; top: 30px; font-size: 15px; line-height: 25px; }
  .bubble--problems .author { left: 170px; top: 110px; }
  .bubble--problems .portrait { left: 20px; top: 20px; width: 138px; height: 110px;
    background: linear-gradient(180deg, #efe27a, #e4d66c); }
  .bubble--problems .tail { left: 520px; top: 128px; }

  .bubble--answer { left: 136px; top: 437px; width: 524px; height: 115px; background: var(--mist); }
  .bubble--answer .quote { left: 34px; top: 28px; font-size: 14px; }
  .bubble--answer .author { left: 306px; top: 95px; }
  .bubble--answer .portrait { left: 395px; top: 0; width: 100px; height: 115px;
    background: radial-gradient(ellipse at 55% 45%, #8f8f8f 0 35%, rgba(233,234,234,0) 70%); }
  .bubble--answer .tail { left: 50px; top: 114px; }

  .bubble--success { left: 100px; top: 592px; width: 597px; height: 185px; background: var(--lime);
    border-radius: 2px; transform: rotate(1.1deg); }
  .bubble--success .quote { left: 158px; top: 30px; font-size: 15.5px; line-height: 24px; }
  .bubble--success .author { right: 44px; top: 154px; }
  .bubble--success .portrait { left: 36px; top: 28px; width: 92px; height: 117px;
    background: linear-gradient(160deg, #6c6c6c, #1e1e1e); }
  .bubble--success .tail { left: 516px; top: 183px; }

  .bubble--action { left: 137px; top: 822px; width: 521px; height: 88px; background: var(--sky); }
  .bubble--action .quote { left: 34px; top: 26px; font-size: 14px; line-height: 21px; }
  .bubble--action .author { left: 224px; top: 67px; }
  .bubble--action .portrait { left: 414px; top: 8px; width: 72px; height: 72px; border-radius: 50%;
    background: radial-gradient(circle at 50% 40%, #9a9a9a, #2c2c2c); }
  .bubble--action .tail { left: 50px; top: 87px; }

  .bubble--onething { left: 127px; top: 948px; width: 570px; height: 145px; background: var(--lavender);
    transform: rotate(-2deg); overflow: visible; }
  .bubble--onething .portrait { left: 0; top: 0; width: 260px; height: 145px; border-radius: 14px 0 0 14px;
    background: linear-gradient(90deg, #8e8a6e 0%, #7a7470 40%, #b4adc4 75%, rgba(209,204,228,0) 100%); }
  .bubble--onething .quote { left: 214px; top: 36px; font-size: 14.5px; line-height: 22px; }
  .bubble--onething .author { left: 218px; top: 112px; }
  .bubble--onething .tail { left: 64px; top: 144px; }
</style>
</head>
<body>
<div class="canvas">
  <div class="poster"></div>

  <div class="bubble bubble--pupil">
    <p class="quote">What the pupil must learn, if he learns anything at all,<br>is that the world will do most of the work for you,<br>provided you cooperate with it by identifying<br>how it really works and aligning with those realities.<br>If we do not let the world teach us, it teaches us a lesson.</p>
    <div class="portrait" role="img" aria-label="Black and white portrait photo of Harold Wexbury"></div>
    <p class="author">-Harold Wexbury</p>
    <svg class="tail" width="40" height="36" viewBox="0 0 40 36"><path d="M0 0 L36 0 Q14 14 4 34 Q10 16 0 0Z" fill="var(--sky)"/></svg>
  </div>

  <div class="bubble bubble--problems">
    <div class="portrait" role="img" aria-label="Line drawing portrait of Tom Harlow"></div>
    <p class="quote">I tackle every big new problem by asking<br>two questions: Who has dealt with this problem well?<br>And what can we learn from them?</p>
    <p class="author">- Tom Harlow</p>
    <svg class="tail" width="30" height="30" viewBox="0 0 30 30"><path d="M0 0 L28 0 L22 26Z" fill="var(--lemon)"/></svg>
  </div>

  <div class="bubble bubble--answer">
    <p class="quote">If we can really understand the problem,<br>the answer will come out of it,<br>because the answer is not separate from the problem.</p>
    <div class="portrait" role="img" aria-label="Halftone dot portrait of Ravindra Pallathuri"></div>
    <p class="author">-Ravindra Pallathuri</p>
    <svg class="tail" width="40" height="36" viewBox="0 0 40 36"><path d="M0 0 L36 0 Q14 14 4 34 Q10 16 0 0Z" fill="var(--mist)"/></svg>
  </div>

  <div class="bubble bubble--success">
    <div class="portrait" role="img" aria-label="Black and white portrait photo of Ned Pilsk"></div>
    <p class="quote">Success is nothing more than a few simple disciplines,<br>practiced every day; while failure is simply<br>a few errors in judgment, repeated every day.<br>It is the accumulative weight of our disciplines and<br>our judgments that leads us to either fortune or failure.</p>
    <p class="author">-Ned Pilsk</p>
    <svg class="tail" width="30" height="30" viewBox="0 0 30 30"><path d="M0 0 L26 0 L18 28Z" fill="var(--lime)"/></svg>
  </div>

  <div class="bubble bubble--action">
    <p class="quote">Inaction breeds doubt and fear.<br>Action breeds confidence and courage.</p>
    <p class="author">-Walt Brimsley</p>
    <div class="portrait" role="img" aria-label="Round black and white portrait photo of Walt Brimsley"></div>
    <svg class="tail" width="40" height="36" viewBox="0 0 40 36"><path d="M0 0 L36 0 Q14 14 4 34 Q10 16 0 0Z" fill="var(--sky)"/></svg>
  </div>

  <div class="bubble bubble--onething">
    <div class="portrait" role="img" aria-label="Colour photo of Lenny Druse smiling, fading into the bubble"></div>
    <p class="quote">What’s the one thing you can do,<br>such that by doing it, everything else<br>will be easier or unnecessary?</p>
    <p class="author">-Lenny Druse</p>
    <svg class="tail" width="40" height="36" viewBox="0 0 40 36"><path d="M0 0 L36 0 Q14 14 4 34 Q10 16 0 0Z" fill="#857d76"/></svg>
  </div>
</div>
</body>
</html>
```